Finance Product Agency Business Card Design

We're an agency that provides products (service contracts, gap insurance, tire and wheel, etc) and support to dealership finance departments. We specialize in training finance producers to maximize their potential and also keep them up to date on the ever changing compliance and legal landscape. I'll attach an image of our logo, excited to see what you all come up with. Would also be interested in discussing our new website design with the winner.

Target Market(s)

auto dealerships

Industry/Entity Type

Business

Contact Information for Business Card

Dale Hoskirk
Phone 517.364.2908
Fax 877.245.3196
email Dale.Hoskirk@brightlanecoverage.com

Requirements
Must have
• basic contact information
Nice to have
• looking for something professional but modern

```html
<!DOCTYPE html>
<html lang="en">
<head>
<meta charset="utf-8">
<title>Brightlane Coverage – Business Card</title>
<link href="https://fonts.googleapis.com/css2?family=Open+Sans:wght@400;600;700&display=swap" rel="stylesheet">
<style>
  :root {
    --backdrop: #4b4d4f;
    --card: #ffffff;
    --teal: #3d5f6e;
    --stripe: #7d8a92;
    --ink: #1f2326;
  }
  * { margin: 0; padding: 0; box-sizing: border-box; }
  html, body { width: 1200px; height: 960px; overflow: hidden; }
  body {
    background: var(--backdrop);
    font-family: "Open Sans", Arial, sans-serif;
    position: relative;
  }
  .card {
    position: absolute;
    background: var(--card);
    border-radius: 34px;
    overflow: hidden;
  }
  .card-front { left: 248px; top: 63px; width: 686px; height: 389px; }
  .card-back  { left: 248px; top: 491px; width: 693px; height: 393px; }

  .brand {
    position: absolute;
    display: flex;
    align-items: center;
    color: var(--teal);
    font-weight: 700;
  }
  .brand-dot {
    border-radius: 50%;
    background: var(--teal);
    flex: none;
  }
  .brand-name { line-height: 1; letter-spacing: 1px; }
  .brand-name span { display: block; }

  .card-front .brand { left: 110px; top: 140px; gap: 28px; }
  .card-front .brand-dot { width: 90px; height: 90px; }
  .card-front .brand-line1 { font-size: 64px; }
  .card-front .brand-line2 { font-size: 29px; letter-spacing: 5px; margin-top: 8px; }

  .back-wave { position: absolute; left: 0; top: 0; width: 693px; height: 393px; }
  .holder-name {
    position: absolute;
    right: 40px; top: 34px;
    color: #ffffff;
    font-weight: 700;
    font-size: 23px;
    letter-spacing: 0.5px;
  }
  .card-back .brand { left: 48px; top: 130px; gap: 18px; }
  .card-back .brand-dot { width: 78px; height: 78px; }
  .card-back .brand-line1 { font-size: 48px; }
  .card-back .brand-line2 { font-size: 21px; letter-spacing: 3.5px; margin-top: 7px; }

  .contact-list {
    position: absolute;
    left: 62px; top: 244px;
    list-style: none;
    color: var(--ink);
    font-size: 17px;
  }
  .contact-list li { display: flex; align-items: center; gap: 10px; height: 32px; }
  .contact-list svg { width: 17px; height: 17px; fill: var(--teal); flex: none; }
</style>
</head>
<body>

<section class="card card-front">
  <div class="brand">
    <div class="brand-dot"></div>
    <div class="brand-name">
      <span class="brand-line1">BRIGHTLANE</span>
      <span class="brand-line2">COVERAGE</span>
    </div>
  </div>
</section>

<section class="card card-back">
  <svg class="back-wave" viewBox="0 0 693 393" preserveAspectRatio="none">
    <path d="M0 0 H693 V200 C520 110 300 40 60 38 C30 38 10 48 0 60 Z" fill="var(--teal)"/>
    <path d="M0 62 C12 48 32 40 60 40 C300 42 520 120 693 210 V236 C520 150 300 52 60 44 C32 44 12 52 0 68 Z" fill="var(--stripe)"/>
    <path d="M0 60 C10 48 30 38 60 38 C300 40 520 110 693 200 V210 C520 120 300 42 60 40 C32 40 12 48 0 62 Z" fill="#ffffff"/>
  </svg>
  <div class="holder-name">Dale Hoskirk</div>

  <div class="brand">
    <div class="brand-dot"></div>
    <div class="brand-name">
      <span class="brand-line1">BRIGHTLANE</span>
      <span class="brand-line2">COVERAGE</span>
    </div>
  </div>

  <ul class="contact-list">
    <li>
      <svg viewBox="0 0 24 24"><path d="M6.6 10.8a15 15 0 0 0 6.6 6.6l2.2-2.2c.3-.3.7-.4 1-.2 1.1.4 2.3.6 3.6.6.6 0 1 .4 1 1V20c0 .6-.4 1-1 1A17 17 0 0 1 3 4c0-.6.4-1 1-1h3.5c.6 0 1 .4 1 1 0 1.3.2 2.5.6 3.6.1.3 0 .7-.2 1z"/></svg>
      517.364.2908
    </li>
    <li>
      <svg viewBox="0 0 24 24"><path d="M6 2h12v5H6z M3 8h18a1 1 0 0 1 1 1v8h-4v-3H6v3H2V9a1 1 0 0 1 1-1z M7 15h10v7H7z"/></svg>
      877.245.3196
    </li>
    <li>
      <svg viewBox="0 0 24 24"><path d="M12 2a10 10 0 1 0 0 20 10 10 0 0 0 0-20zm7.9 9h-3.4a15 15 0 0 0-1.4-6.2A8 8 0 0 1 19.9 11zM12 4c.9 1.2 2.2 3.6 2.5 7h-5C9.8 7.6 11.1 5.2 12 4zM8.9 4.8A15 15 0 0 0 7.5 11H4.1a8 8 0 0 1 4.8-6.2zM4.1 13h3.4a15 15 0 0 0 1.4 6.2A8 8 0 0 1 4.1 13zM12 20c-.9-1.2-2.2-3.6-2.5-7h5c-.3 3.4-1.6 5.8-2.5 7zm3.1-.8a15 15 0 0 0 1.4-6.2h3.4a8 8 0 0 1-4.8 6.2z"/></svg>
      brightlanecoverage.com
    </li>
    <li>
      <svg viewBox="0 0 24 24"><path d="M2 9l10-6 10 6v11a1 1 0 0 1-1 1H3a1 1 0 0 1-1-1z M4 10l8 5 8-5-8-4.8z"/></svg>
      Dale.Hoskirk@brightlanecoverage.com
    </li>
  </ul>
</section>

</body>
</html>
```